Letterhead

We have a new logo and would like to design electronic letterhead with our new logo. We have two office locations. One of our offices is moving in July.

```html
<!DOCTYPE html>
<html lang="en">
<head>
<meta charset="utf-8">
<title>KDLW Letterhead</title>
<link rel="stylesheet" href="https://fonts.googleapis.com/css2?family=Montserrat:wght@400&family=Roboto:wght@400&display=swap">
<style>
  :root {
    --backdrop: #e9e6e1;
    --paper: #ffffff;
    --brand-blue: #2f74bb;
    --brand-dark: #353334;
    --brand-grey: #d4d5d7;
    --ink: #333333;
  }
  * { margin: 0; padding: 0; box-sizing: border-box; }
  html, body {
    width: 1200px;
    height: 1200px;
    overflow: hidden;
    background: var(--backdrop);
  }
  .canvas {
    position: relative;
    width: 1200px;
    height: 1200px;
  }
  .letterhead {
    position: absolute;
    left: 246px;
    top: 125px;
    width: 707px;
    height: 915px;
    background: var(--paper);
    box-shadow: 0 6px 16px rgba(0,0,0,0.16);
    overflow: hidden;
  }
  .corner-bands {
    position: absolute;
    left: 0;
    top: 0;
    width: 707px;
    height: 915px;
  }
  .firm-name {
    position: absolute;
    left: 52px;
    top: 48px;
    font-family: "Montserrat", sans-serif;
    font-weight: 400;
    font-size: 84px;
    line-height: 1;
    letter-spacing: -3px;
    color: var(--brand-dark);
  }
  .contact-list {
    position: absolute;
    right: 56px;
    top: 746px;
    list-style: none;
  }
  .contact-item {
    display: flex;
    align-items: center;
    justify-content: flex-end;
    gap: 11px;
    height: 22px;
    margin-bottom: 8px;
    font-family: "Roboto", sans-serif;
    font-size: 11px;
    color: var(--ink);
  }
  .contact-icon {
    width: 21px;
    height: 21px;
    flex: none;
  }
  .contact-icon rect,
  .contact-icon path,
  .contact-icon circle {
    fill: none;
    stroke: var(--brand-blue);
    stroke-width: 1.2;
    stroke-linejoin: round;
    stroke-linecap: round;
  }
</style>
</head>
<body>
<div class="canvas">
  <div class="letterhead">
    <svg class="corner-bands" viewBox="0 0 707 915" aria-hidden="true">
      <!-- top right: diagonal band with corner triangle -->
      <polygon fill="var(--brand-grey)" points="470,0 525,0 707,182 707,237"/>
      <polygon fill="var(--brand-blue)" points="565,0 707,0 707,142"/>
      <!-- bottom left: diagonal band with corner triangle -->
      <polygon fill="var(--brand-blue)" points="0,680 0,735 180,915 235,915"/>
      <polygon fill="var(--brand-dark)" points="0,775 0,915 140,915"/>
    </svg>

    <div class="firm-name">KDLW</div>

    <ul class="contact-list">
      <li class="contact-item">
        <span>48 Harlow St. Eastfield</span>
        <svg class="contact-icon" viewBox="0 0 26 26" aria-hidden="true">
          <rect x="1" y="1" width="24" height="24" rx="4"/>
          <path d="M13 20 C9 15 8 12.5 8 10.5 A5 5 0 0 1 18 10.5 C18 12.5 17 15 13 20 Z"/>
          <circle cx="13" cy="10.5" r="1.8"/>
        </svg>
      </li>
      <li class="contact-item">
        <span>+1 555 0142</span>
        <svg class="contact-icon" viewBox="0 0 26 26" aria-hidden="true">
          <rect x="1" y="1" width="24" height="24" rx="4"/>
          <path d="M8 6 L10.5 6 L12 10 L10.3 11.3 C11.2 13.3 12.7 14.8 14.7 15.7 L16 14 L20 15.5 L20 18 C20 19 19 20 18 20 C12 19.5 6.5 14 6 8 C6 7 7 6 8 6 Z"/>
          <path d="M15 6.5 A5 5 0 0 1 19.5 11"/>
        </svg>
      </li>
      <li class="contact-item">
        <span>OFFICE@KDLW.COM</span>
        <svg class="contact-icon" viewBox="0 0 26 26" aria-hidden="true">
          <rect x="1" y="1" width="24" height="24" rx="4"/>
          <rect x="6" y="9" width="14" height="10" rx="1"/>
          <path d="M6 10 L13 15 L20 10"/>
          <circle cx="13" cy="6.5" r="1.8"/>
        </svg>
      </li>
      <li class="contact-item">
        <span>WWW.KDLW.COM</span>
        <svg class="contact-icon" viewBox="0 0 26 26" aria-hidden="true">
          <rect x="1" y="1" width="24" height="24" rx="4"/>
          <circle cx="13" cy="13" r="7"/>
          <path d="M6 13 L20 13 M13 6 C10.5 9 10.5 17 13 20 M13 6 C15.5 9 15.5 17 13 20"/>
        </svg>
      </li>
    </ul>
  </div>
</div>
</body>
</html>
```